Bluewater Getaways KT needs a new Website

We have an old website that is just that - old. We need a fresh website that is professional graphic designed that has the following features.
1. Can be updated by ourselves in some areas.
2. Has a shopping cart.
3. Has links to download PDF files
4. Has links to other pages in the website
5. Includes social media links
6. Has a client log-in area
Full details in brief provided.

SORRY BUT IT'S URGENT. We've taken too long to write the details and it is now urgent. So my apologies I will be asking for designers to work quickly.

We will continue to use our existing web hosting company and url. Their is a link to the old website in the Design Brief.
Updates

UPDATE:  Please see the new file UPDATE TO DESIGN BRIEF.
Thanks for all your submissions to date.  We hope the update will assist with your designs.
As indicated in previous messages, we are happy with the Home Page + 1 Page in order to select the designer to work with in creating the full design. 

Thankyou Designers.  Much appreciate your efforts.
It's getting late here on Norfolk so I won't have much chance too review any more designs this evening.
But for your information:
Designer 7318405 Ravindra Mehta is so far the closest to what we are seeking.
Thanks again. 

Reason: Have extended to Monday 7 October to give time for designers to submit after feedback today. Especially given the time differences

Target Market(s)

Very wide audience. Current client group not that tech savvy, but we hope to broaden our market and sell more creative products, and so website needs to consider how people now use media, ie tablets & iphones.

Industry/Entity Type

Shopping

Requirements
Nice to have
• PLEASE SEE THE "UPDATE TO THE DESIGN BRIEF"

```html
<!DOCTYPE html>
<html lang="en">
<head>
<meta charset="utf-8">
<title>Bluewater Getaways KT</title>
<link rel="stylesheet" href="https://fonts.googleapis.com/css2?family=Open+Sans:wght@400;600;700&family=Raleway:wght@300&display=swap">
<style>
  :root {
    --sepia-light: #efe6d8;
    --sepia-mid: #cdb69a;
    --sepia-dark: #8a7560;
    --nav-bg: rgba(22, 18, 14, 0.88);
    --white: #ffffff;
    --ink: #111111;
    --body-text: #3c3a37;
    --brand-orange: #f5821f;
    --button-grey: #9c9894;
    --footer-line: #d7d2cb;
  }
  * { box-sizing: border-box; margin: 0; padding: 0; }
  html, body { width: 1200px; height: 728px; overflow: hidden; }
  body {
    position: relative;
    font-family: "Open Sans", sans-serif;
    background: var(--white);
  }
  .hero-photo {
    position: absolute; inset: 0 0 85px 0;
    background:
      radial-gradient(ellipse 220px 160px at 770px 190px, rgba(255,255,255,0.35), transparent 70%),
      radial-gradient(ellipse 340px 160px at 1050px 40px, rgba(90,70,50,0.55), transparent 70%),
      linear-gradient(180deg, var(--sepia-dark) 0%, var(--sepia-mid) 30%, #dccab2 60%, var(--sepia-light) 85%, #f6f2ec 100%);
  }
  .brand {
    position: absolute; left: 38px; top: 52px;
    display: flex; align-items: center; gap: 10px;
    font-size: 22px; font-weight: 700; color: var(--brand-orange);
  }
  .brand-dot { width: 34px; height: 34px; border-radius: 50%; background: var(--brand-orange); }
  .utility {
    position: absolute; right: 38px; top: 17px;
    display: flex; align-items: center; gap: 8px;
    font-size: 16px; color: var(--white);
  }
  .utility svg { margin-right: 4px; }
  .main-nav {
    position: absolute; left: 490px; right: 0; top: 47px; height: 38px;
    background: var(--nav-bg);
    border-radius: 19px 0 0 19px;
    display: flex; align-items: center; padding-left: 23px; gap: 19px;
  }
  .main-nav a {
    position: relative;
    color: var(--white); text-decoration: none; font-size: 16px;
  }
  .main-nav a.has-menu::after {
    content: ""; position: absolute; left: 50%; bottom: -6px; margin-left: -3px;
    border: 3px solid transparent; border-top-color: var(--white);
  }
  .intro {
    position: absolute; top: 318px; left: 0; right: 0; text-align: center;
  }
  .intro h1 {
    font-family: "Raleway", sans-serif; font-weight: 300;
    font-size: 60px; letter-spacing: -1px; color: var(--ink);
    text-shadow: 2px 2px 0 var(--white);
    line-height: 1.1;
  }
  .intro p {
    font-size: 13px; font-weight: 600; color: var(--ink); line-height: 28px;
    text-shadow: 1px 1px 0 var(--white);
  }
  .pillars {
    position: absolute; top: 483px; left: 0; width: 1200px;
  }
  .pillar {
    position: absolute; width: 220px; margin-left: -110px; text-align: center;
  }
  .pillar h2 { font-size: 19px; font-weight: 700; color: var(--ink); margin-bottom: 10px; }
  .pillar p { font-size: 14px; line-height: 16px; color: var(--body-text); margin-bottom: 20px; }
  .pillar a {
    display: inline-block; padding: 1px 9px; border-radius: 9px;
    background: var(--button-grey); color: var(--white);
    font-size: 12px; text-decoration: none;
  }
  .pillar a.is-active { background: var(--brand-orange); }
  .site-footer {
    position: absolute; left: 0; right: 0; top: 643px; bottom: 0;
    border-top: 1px solid var(--footer-line);
    background: linear-gradient(180deg, rgba(255,255,255,0.4), var(--white));
  }
  .contact {
    position: absolute; left: 36px; top: 33px; font-size: 14px; color: var(--ink);
  }
  .social {
    position: absolute; left: 197px; top: 30px; display: flex; gap: 4px;
  }
  .social span { width: 22px; height: 22px; border-radius: 50%; background: var(--ink); }
  .copyright {
    position: absolute; right: 53px; top: 33px; font-size: 14px; color: var(--ink);
  }
</style>
</head>
<body>
  <div class="hero-photo" role="img" aria-label="Sepia photograph of a person paddling a kayak on clear shallow water beside rocks"></div>

  <div class="brand"><span class="brand-dot"></span>Bluewater Getaways KT</div>

  <div class="utility">
    <svg width="18" height="16" viewBox="0 0 18 16" fill="none" stroke="#fff" stroke-width="1.3">
      <path d="M1 2h3l2 8h9l2-6H5"/><circle cx="7.5" cy="13.5" r="1.3"/><circle cx="14" cy="13.5" r="1.3"/>
    </svg>
    <span>Shopping Cart</span><span>|</span><span>Login</span>
  </div>

  <nav class="main-nav">
    <a href="#">Home</a>
    <a href="#" class="has-menu">Overview</a>
    <a href="#">Norfolk&nbsp; Island</a>
    <a href="#" class="has-menu">Services</a>
    <a href="#">Our Shop</a>
    <a href="#">Make a Booking</a>
    <a href="#">Testimonials</a>
  </nav>

  <section class="intro">
    <h1>OUR SOCIAL ENTERPRISE</h1>
    <p>ESTABLISHED JULY 2001,</p>
    <p>--------PROMOTES----------</p>
  </section>

  <section class="pillars">
    <div class="pillar" style="left:232px">
      <h2>Diversity</h2>
      <p>Lorem ipsum dolor sit amet, adipisicing elit, sed do labore</p>
      <a href="#" class="is-active">More Details</a>
    </div>
    <div class="pillar" style="left:476px">
      <h2>Caring</h2>
      <p>Lorem ipsum dolor sit amet, adipisicing elit, sed do labore</p>
      <a href="#">More Details</a>
    </div>
    <div class="pillar" style="left:718px">
      <h2>Community</h2>
      <p>Lorem ipsum dolor sit amet, adipisicing elit, sed do labore</p>
      <a href="#">More Details</a>
    </div>
    <div class="pillar" style="left:967px">
      <h2>Norfolk Island</h2>
      <p>Lorem ipsum dolor sit amet, adipisicing elit, sed do labore</p>
      <a href="#">More Details</a>
    </div>
  </section>

  <footer class="site-footer">
    <div class="contact">Call us&nbsp; + 61 20 55 0147</div>
    <div class="social" aria-label="Social media links">
      <span></span><span></span><span></span><span></span>
    </div>
    <div class="copyright">© 2013 All Right Reserved</div>
  </footer>
</body>
</html>
```